Newsletter Header - Insert Cutting Branch

We have a Hensley Family Foundation (HFF) Logo (see attached) and are creating a Newsletter with the title: The Green Thread. The founders of the HFF were nursery people and started their plants via cuttings. So, we want to take a branch from the HFF logo tree and attach it somewhere in the Newsletter title. You can leave the logo as it is - just want a cutting somewhere in the title. The Green Thread title should be 3-D

Target Market(s)

Donors to our Foundation

Industry/Entity Type

Non Profit

Colors

Designer to choose colors to be used in the design.

Requirements
Must have
• Logo remain as is - just a branch duplicate on the header.
Nice to have
• The Green Thread would be nice to have as a 3-D image

```html
<!DOCTYPE html>
<html lang="en">
<head>
<meta charset="utf-8">
<title>The Green Thread – Hensley Family Foundation Newsletter</title>
<link rel="stylesheet" href="https://fonts.googleapis.com/css2?family=Archivo:wght@500&family=Archivo+Black&display=swap">
<style>
  :root {
    --band-top: #2f9a52;
    --band-mid: #6cc07c;
    --band-low: #c9ead0;
    --band-base: #ffffff;
    --org-ink: #4b5752;
    --title-face: #dff05c;
    --title-depth: #6f8a16;
    --title-shade: #3d5208;
    --title-edge: #27360a;
    --sprig-dark: #3f4a38;
    --sprig-light: #7c8a6c;
  }
  html, body {
    margin: 0;
    padding: 0;
    overflow: hidden;
  }
  body {
    width: 1200px;
    height: 244px;
  }
  .newsletter-header {
    position: relative;
    width: 1200px;
    height: 244px;
    overflow: hidden;
    background: linear-gradient(to bottom,
      var(--band-top) 0%,
      var(--band-mid) 45%,
      var(--band-low) 82%,
      var(--band-base) 100%);
  }
  .org-name {
    position: absolute;
    left: 30px;
    top: 88px;
    display: flex;
    align-items: center;
    gap: 22px;
  }
  .org-name__circle {
    width: 84px;
    height: 84px;
    flex: none;
  }
  .org-name__text {
    margin: 0;
    font-family: "Archivo", Arial, sans-serif;
    font-weight: 500;
    font-size: 19px;
    line-height: 24px;
    letter-spacing: 0.08em;
    text-transform: uppercase;
    color: var(--org-ink);
  }
  .title-sprig {
    position: absolute;
    left: 742px;
    top: 14px;
    width: 96px;
    height: 100px;
  }
  .newsletter-title {
    position: absolute;
    left: 322px;
    top: 88px;
    margin: 0;
    font-family: "Archivo Black", "Arial Black", sans-serif;
    font-weight: 400;
    font-size: 76px;
    line-height: 1;
    letter-spacing: 0.01em;
    white-space: nowrap;
    color: var(--title-face);
    transform: scaleY(1.3);
    transform-origin: left top;
    -webkit-text-stroke: 1px var(--title-edge);
    text-shadow:
      1px 1px 0 var(--title-depth),
      2px 2px 0 var(--title-depth),
      3px 3px 0 var(--title-depth),
      4px 4px 0 var(--title-shade),
      5px 5px 0 var(--title-shade),
      6px 6px 0 var(--title-shade),
      7px 7px 0 var(--title-edge),
      9px 9px 6px rgba(0, 0, 0, 0.35);
  }
</style>
</head>
<body>
  <header class="newsletter-header">
    <div class="org-name">
      <svg class="org-name__circle" viewBox="0 0 84 84" aria-hidden="true">
        <circle cx="42" cy="42" r="39" fill="none" stroke="#4b5752" stroke-width="3"/>
      </svg>
      <p class="org-name__text">Hensley<br>Family<br>Foundation</p>
    </div>

    <svg class="title-sprig" viewBox="0 0 96 100" role="img" aria-label="Cutting branch taken from the foundation's tree, attached to the title">
      <defs>
        <linearGradient id="sprigTone" x1="0" y1="0" x2="1" y2="1">
          <stop offset="0" stop-color="#3f4a38"/>
          <stop offset="1" stop-color="#7c8a6c"/>
        </linearGradient>
      </defs>
      <rect x="0" y="0" width="96" height="100" rx="40" fill="url(#sprigTone)" opacity="0.55"/>
    </svg>

    <h1 class="newsletter-title">The Green Thread.</h1>
  </header>
</body>
</html>
```